The Rounded Court Performer Image Design

We are a basketball training company with in-person and online courses and camps for players from 4th grade through college, plus coaches of all levels. We are looking for a modern design of "The Rounded Court Performer" as the attached quick sketch shows. The seven "elements" of the complete player include: 1. Basketball IQ 2. Leadership 3. Mindset 4. Skills 5. Athleticism 6. Habits and 7. Communication
We will plan to use this design on our website, social media, emails, etc. Please see our website at trevanhoops.com to learn more about us and our current branding, fonts, and colors. We prefer to use the orange hex #f15d22 and blacks and dark gray. Though we have teal on our current website, we are moving away from that color so you can leave that off any designs. Thanks!
Target Market(s)
Basketball players and coaches, parents

```html
<!DOCTYPE html>
<html lang="en">
<head>
<meta charset="utf-8">
<title>The Rounded Court Performer</title>
<link rel="stylesheet" href="https://fonts.googleapis.com/css2?family=Exo+2:wght@400&family=Open+Sans:wght@400;600&display=swap">
<style>
  :root {
    --backdrop: #808080;
    --orange: #f15d22;
    --orange-soft: #f0803a;
    --ink: #1b1b1b;
    --dark-gray: #4a4a4d;
    --circle-gray: #e6e6e8;
    --paper: #ffffff;
    --url-gray: #e4e4e4;
  }
  html, body {
    margin: 0;
    padding: 0;
    width: 1200px;
    height: 911px;
    overflow: hidden;
    background: var(--backdrop);
  }
  .flyer {
    position: absolute;
    left: 296px;
    top: 25px;
    width: 647px;
    height: 917px;
    transform: scale(0.938);
    transform-origin: top left;
    background: linear-gradient(180deg, var(--paper) 0%, #f4f4f5 70%, #eaeaeb 100%);
    overflow: hidden;
  }
  .flyer-art {
    position: absolute;
    inset: 0;
    width: 647px;
    height: 917px;
  }
  .title {
    position: absolute;
    writing-mode: vertical-rl;
    font-family: "Exo 2", sans-serif;
    font-weight: 400;
    line-height: 1;
    margin: 0;
    white-space: nowrap;
  }
  .title-top {
    left: 106px;
    top: 62px;
    font-size: 46px;
    color: var(--ink);
  }
  .title-main {
    left: 42px;
    top: 56px;
    font-size: 58px;
    color: var(--orange-soft);
  }
  .elements {
    list-style: none;
    margin: 0;
    padding: 0;
  }
  .element {
    position: absolute;
    font-family: "Open Sans", sans-serif;
    font-weight: 600;
    font-size: 26px;
    color: var(--ink);
    line-height: 1;
    white-space: nowrap;
  }
  .site-url {
    position: absolute;
    left: 0;
    width: 647px;
    top: 858px;
    text-align: center;
    font-family: "Open Sans", sans-serif;
    font-size: 20px;
    letter-spacing: 7px;
    color: var(--url-gray);
    margin: 0;
  }
</style>
</head>
<body>
  <main class="flyer">
    <svg class="flyer-art" viewBox="0 0 647 917" xmlns="http://www.w3.org/2000/svg">
      <defs>
        <linearGradient id="figure-fill" x1="0" y1="0" x2="0" y2="1">
          <stop offset="0" stop-color="#2a2a2a"/>
          <stop offset="0.45" stop-color="#f0803a"/>
          <stop offset="0.75" stop-color="#f0803a"/>
          <stop offset="1" stop-color="#1e1e1e"/>
        </linearGradient>
      </defs>
      <circle class="backdrop-circle" cx="80" cy="300" r="348" fill="var(--circle-gray)"/>
      <circle class="elements-ring" cx="80" cy="300" r="368" fill="none" stroke="var(--orange-soft)" stroke-width="2"/>
      <g class="ring-dots" fill="var(--orange-soft)">
        <circle cx="401" cy="105" r="7"/>
        <circle cx="432" cy="193" r="7"/>
        <circle cx="443" cy="278" r="7"/>
        <circle cx="435" cy="360" r="7"/>
        <circle cx="407" cy="446" r="7"/>
        <circle cx="248" cy="624" r="7"/>
      </g>
      <path class="footer-band" d="M0 762 C 90 738, 190 760, 300 788 C 400 812, 520 808, 647 752 L 647 917 L 0 917 Z" fill="var(--dark-gray)"/>
      <path class="footer-accent" d="M0 756 C 90 732, 190 754, 300 782 C 400 806, 520 802, 647 752 L 647 760 C 520 812, 400 818, 300 792 C 190 764, 90 744, 0 768 Z" fill="var(--orange)"/>
      <rect class="player-figure" role="img" aria-label="Silhouette of a basketball player in an orange jersey spinning a ball on one raised finger" x="250" y="78" width="160" height="760" rx="60" fill="url(#figure-fill)"/>
    </svg>

    <h1 class="title title-top">The Rounded</h1>
    <h1 class="title title-main">Court Performer</h1>

    <ul class="elements">
      <li class="element" style="right:32px; top:90px;">Basketball IQ</li>
      <li class="element" style="right:39px; top:176px;">Leadership</li>
      <li class="element" style="right:39px; top:262px;">Mindset</li>
      <li class="element" style="right:39px; top:347px;">Skills</li>
      <li class="element" style="right:39px; top:433px;">Athleticism</li>
      <li class="element" style="right:32px; top:519px;">Habits</li>
      <li class="element" style="right:32px; top:604px;">Communication</li>
    </ul>

    <p class="site-url">www.trevanhoops.com</p>
  </main>
</body>
</html>
```